Financial Planning firm focused on serving women 55-65 yrs old needs stationary design

We are rebranding our financial planning firm and our target client is a 55-65 yr old women. We need a stationary design to go with our new logo.

Contact Information: Raymond Kessler, MS, CFP President Harlow Wealth Management 4820 Bramblewood Lane, Suite 317 Estero, FL 33961 ray@harlowwealthmgmt.example phone 239-555-0184

```html
<!DOCTYPE html>
<html lang="en">
<head>
<meta charset="utf-8">
<title>Harlow Wealth Management – Business Cards</title>
<link rel="stylesheet" href="https://fonts.googleapis.com/css2?family=Roboto:wght@300;400&display=swap">
<style>
  :root {
    --backdrop: #e9e8e4;
    --card: #f1f1ef;
    --sage: #8fa68a;
    --sage-tint: #dfe4dc;
    --navy: #2f5a7e;
    --ink: #3a3a3a;
  }
  * { margin: 0; padding: 0; box-sizing: border-box; }
  html, body { width: 1200px; height: 900px; overflow: hidden; }
  body {
    background: var(--backdrop);
    font-family: "Roboto", Arial, sans-serif;
    font-weight: 300;
    color: var(--ink);
    display: flex;
    align-items: center;
    justify-content: center;
    gap: 90px;
  }
  .card {
    position: relative;
    width: 400px;
    height: 700px;
    background: var(--card);
    box-shadow: 0 2px 8px rgba(0,0,0,0.12);
    overflow: hidden;
  }
  .card-pattern { position: absolute; inset: 0; }
  .brand-circle {
    position: absolute;
    border-radius: 50%;
    background: var(--sage);
  }

  /* Front */
  .card-front .brand-circle { width: 170px; height: 170px; left: 95px; top: 190px; }
  .wordmark {
    position: absolute;
    left: 95px;
    top: 385px;
    width: 230px;
    color: var(--navy);
    font-weight: 400;
    text-transform: uppercase;
  }
  .wordmark-main { display: block; font-size: 52px; line-height: 1; letter-spacing: 8px; }
  .wordmark-rule { height: 1px; background: var(--navy); margin: 10px 0 6px; }
  .wordmark-sub { display: block; font-size: 13px; letter-spacing: 2.5px; text-align: right; }

  /* Back */
  .card-back .brand-circle { width: 165px; height: 165px; left: 36px; top: 40px; }
  .contact-block { position: absolute; left: 36px; right: 30px; top: 270px; }
  .person-name { font-size: 24px; color: var(--navy); }
  .person-title { font-size: 15px; margin-top: 3px; }
  .rule { height: 1px; background: var(--navy); margin: 14px -30px 24px 28px; }
  .contact-lines { font-size: 15px; line-height: 1.45; padding-left: 28px; }
  .contact-lines .label { color: var(--navy); display: inline-block; width: 20px; margin-left: -20px; }
  .address { font-size: 15px; line-height: 1.5; margin-top: 22px; padding-left: 28px; }
  .website { font-size: 15px; color: var(--navy); margin-top: 28px; padding-left: 28px; }
</style>
</head>
<body>
  <section class="card card-front">
    <svg class="card-pattern" width="400" height="700" viewBox="0 0 400 700" role="img" aria-label="Fine diagonal stripe pattern across the top and bottom of the card">
      <polygon points="0,0 400,0 400,60 0,230" fill="var(--sage-tint)"/>
      <polygon points="400,470 400,700 0,700 0,640" fill="var(--sage-tint)"/>
    </svg>
    <div class="brand-circle"></div>
    <div class="wordmark">
      <span class="wordmark-main">Harlow</span>
      <div class="wordmark-rule"></div>
      <span class="wordmark-sub">Wealth Management</span>
    </div>
  </section>

  <section class="card card-back">
    <div class="brand-circle"></div>
    <div class="contact-block">
      <div class="person-name">Raymond Kessler, MS, CFP</div>
      <div class="person-title">President Harlow Wealth Management</div>
      <div class="rule"></div>
      <div class="contact-lines">
        <div><span class="label">T</span>239-555-0184</div>
        <div><span class="label">E</span>ray@harlowwealthmgmt.example</div>
      </div>
      <div class="address">4820 Bramblewood Lane<br>Suite 317 Estero, FL 33961</div>
      <div class="website">harlowwealthmgmt.example</div>
    </div>
  </section>
</body>
</html>
```